Postcard Design Project

I am an answering service and appointment scheduler for various Real Estate Appraisers around the country. This is for soliciting new clients.

Industry/Entity Type

Real Estate

```html
<!DOCTYPE html>
<html lang="en">
<head>
<meta charset="utf-8">
<title>The Valuer's Aide – Postcard</title>
<link rel="stylesheet" href="https://fonts.googleapis.com/css2?family=Cinzel:wght@700&family=Jost:wght@400&family=Montserrat:wght@800&family=Oswald:wght@500;600&display=swap">
<style>
  :root{
    --page:#e9ebee;
    --blue:#1565c8;
    --blue-deep:#0b4fa8;
    --navy:#1a2e55;
    --sky-light:#f4f8fc;
    --sky:#7ec0f0;
    --grey-panel:#f3f3f3;
    --silver:#a9abae;
    --ink:#222;
    --white:#fff;
  }
  *{box-sizing:border-box;margin:0;padding:0}
  html,body{width:864px;height:1200px;overflow:hidden;background:var(--page)}
  .card{position:absolute;left:66px;width:732px;height:528px;overflow:hidden;box-shadow:0 2px 8px rgba(0,0,0,.25)}
  .card--front{top:55px;background:linear-gradient(100deg,var(--sky-light) 0%,#d9ecfa 45%,var(--sky) 100%)}
  .card--back{top:628px;background:var(--white)}
  .shapes{position:absolute;inset:0}
  .brand{position:absolute;display:flex;align-items:center;gap:8px;font-family:"Cinzel",serif;font-weight:700;color:var(--blue)}
  .brand__mark{width:14px;height:14px;background:var(--blue)}
  .brand--front{left:49px;top:68px;font-size:25px}
  .brand--back{left:414px;top:72px;font-size:18px}
  .tagline{position:absolute;left:300px;top:44px;width:400px;text-align:center;font-family:"Cinzel",serif;font-weight:700;font-size:21px;line-height:30px;color:var(--navy)}
  .services__title{position:absolute;left:57px;top:152px;font-family:"Montserrat",sans-serif;font-weight:800;font-size:23px;color:var(--blue-deep)}
  .services__list{position:absolute;left:58px;top:192px;list-style:none;font-family:"Jost",sans-serif;font-size:14px;line-height:21px;color:var(--ink)}
  .services__list li{display:flex;align-items:center;gap:6px}
  .services__list svg{width:11px;height:11px}
  .photo{position:absolute;left:420px;top:100px;width:312px;height:320px;border-radius:40px 0 0 0;background:linear-gradient(160deg,#d9573f 0%,#f2e3c4 40%,#e2b79a 75%,#c98f72 100%)}
  .offer{position:absolute;left:51px;top:443px;font-family:"Oswald",sans-serif;color:var(--white);text-transform:uppercase}
  .offer__intro{font-weight:500;font-size:17px;line-height:22px}
  .offer__regular{font-weight:600;font-size:28px;line-height:34px}
  .call-box{position:absolute;left:484px;top:440px;width:199px;height:63px;border:1px solid var(--white);text-align:center;font-family:"Oswald",sans-serif;color:var(--white)}
  .call-box__label{font-weight:600;font-size:28px;line-height:32px;padding-top:2px}
  .call-box__phone{font-family:"Montserrat",sans-serif;font-weight:800;font-size:19px;line-height:24px}
  .honest{position:absolute;left:49px;top:40px;width:300px}
  .honest__title{font-family:"Jost",sans-serif;font-size:20px;color:var(--blue-deep);margin-bottom:10px}
  .honest__text{font-family:"Jost",sans-serif;font-size:14.5px;line-height:19.5px;color:var(--ink)}
  .call-band{position:absolute;left:49px;top:288px;color:var(--white)}
  .call-band__label{font-family:"Montserrat",sans-serif;font-weight:800;font-size:41px;line-height:48px}
  .call-band__phone{font-family:"Oswald",sans-serif;font-weight:600;font-size:54px;line-height:60px;letter-spacing:-.5px}
  .address{position:absolute;left:420px;top:126px;width:152px;text-align:center;font-family:"Jost",sans-serif;font-size:14px;line-height:18px;color:var(--ink)}
</style>
</head>
<body>

<section class="card card--front">
  <div class="photo" role="img" aria-label="Photo of an open hand holding a small model house with a red roof against blue sky"></div>
  <svg class="shapes" viewBox="0 0 732 528" aria-hidden="true">
    <path d="M0 362 Q330 440 732 290 L732 300 Q330 452 0 374 Z" fill="var(--silver)"/>
    <path d="M0 374 Q330 452 732 300 L732 528 L0 528 Z" fill="var(--blue)"/>
  </svg>
  <div class="brand brand--front"><span class="brand__mark"></span>The Valuer's Aide</div>
  <h1 class="tagline">We Take Care of the Office<br>So you can…Well…Appraise!</h1>
  <h2 class="services__title">WHAT WE DO FOR YOU:</h2>
  <ul class="services__list">
    <li><svg viewBox="0 0 12 12"><path d="M1 6l3.5 3.5L11 2" fill="none" stroke="var(--blue-deep)" stroke-width="2"/></svg>Answer your phone calls.</li>
    <li><svg viewBox="0 0 12 12"><path d="M1 6l3.5 3.5L11 2" fill="none" stroke="var(--blue-deep)" stroke-width="2"/></svg>Set-up your appointments.</li>
    <li><svg viewBox="0 0 12 12"><path d="M1 6l3.5 3.5L11 2" fill="none" stroke="var(--blue-deep)" stroke-width="2"/></svg>Answer your e-mail.</li>
    <li><svg viewBox="0 0 12 12"><path d="M1 6l3.5 3.5L11 2" fill="none" stroke="var(--blue-deep)" stroke-width="2"/></svg>Update AMC's and Clients.</li>
    <li><svg viewBox="0 0 12 12"><path d="M1 6l3.5 3.5L11 2" fill="none" stroke="var(--blue-deep)" stroke-width="2"/></svg>Update licenses and E&amp;O.</li>
    <li><svg viewBox="0 0 12 12"><path d="M1 6l3.5 3.5L11 2" fill="none" stroke="var(--blue-deep)" stroke-width="2"/></svg>Prep your reports with pertinent data.</li>
    <li><svg viewBox="0 0 12 12"><path d="M1 6l3.5 3.5L11 2" fill="none" stroke="var(--blue-deep)" stroke-width="2"/></svg>Provide plat maps, zoning, field cards &amp;</li>
    <li><svg viewBox="0 0 12 12"><path d="M1 6l3.5 3.5L11 2" fill="none" stroke="var(--blue-deep)" stroke-width="2"/></svg>MLS sheets to your work file.</li>
  </ul>
  <div class="offer">
    <p class="offer__intro">All for the low introductory price of $67 per order.</p>
    <p class="offer__regular">Regularly $79 a 15% savings!!!</p>
  </div>
  <div class="call-box">
    <p class="call-box__label">CALL TODAY!!!</p>
    <p class="call-box__phone">401-555-0147</p>
  </div>
</section>

<section class="card card--back">
  <svg class="shapes" viewBox="0 0 732 528" aria-hidden="true">
    <path d="M0 0 L250 0 Q410 230 270 528 L0 528 Z" fill="var(--grey-panel)"/>
    <path d="M250 0 L272 0 Q432 235 292 528 L270 528 Q410 230 250 0 Z" fill="var(--silver)"/>
    <path d="M272 0 L300 0 Q458 250 292 528 L284 528 Q430 240 272 0 Z" fill="var(--blue)"/>
    <path d="M0 282 L378 282 Q372 340 352 397 L0 397 Z" fill="var(--blue)"/>
  </svg>
  <div class="honest">
    <h2 class="honest__title">Let's Be Honest:</h2>
    <p class="honest__text">It is impossible to be really good<br>at two things simultaneously.<br>Focusing on one neglects the<br>other and vice versa. Without a lot<br>of outside help, running an effective<br>small business AND continuing to be<br>a really great appraiser is not really an<br>option. This is where the services of<br>The Valuer's Aide can help.</p>
  </div>
  <div class="call-band">
    <p class="call-band__label">CALL TODAY!!</p>
    <p class="call-band__phone">401-555-0147</p>
  </div>
  <div class="brand brand--back"><span class="brand__mark"></span>The Valuer's Aide</div>
  <p class="address">14 Linden Court<br>Westbrook, RI 02899</p>
</section>

</body>
</html>
```